Brand and Programs Diagram

We want to present our Brands and Programs in a diagram.

Attached are a couple of examples of ideas of how we see it could be presented
Logos all attached
Similar colours and fonts

Instructions
Maple Grove Kindergarten logo In the middle and biggest
Feeds to
a heading in top right
Bloom Pathway 2.0 Curriculum
then five pillars below and their logos
Keen Steps
Curious
Gather
Move
Tribe

Then to the left
Have a heading
Brands & Programs

Have lines feeding from the Maple Grove Kindergarten logo to each of the Brand & Programs logos

Kestrel

Nest +

Tots +

DOVE

WREN

If there is a way of colour coding shading or making the DOVE, WREN, and Tribe logos connect in some way would be ideal as they are all part of the same family

At the very top if we could add the Maple Grove Education logo and have it feed into the Maple Grove Kindergarten logo.

```html
<!DOCTYPE html>
<html lang="en">
<head>
<meta charset="utf-8">
<title>Maple Grove Kindergarten – Brands &amp; Programs</title>
<link rel="stylesheet" href="https://fonts.googleapis.com/css2?family=Roboto+Condensed:wght@300;400;700&family=Raleway:wght@400&display=swap">
<style>
  :root {
    --navy: #3a78b5;
    --ocean: #3a9ec2;
    --teal: #3ab5c2;
    --jade: #3bb894;
    --leaf: #7cc160;
    --sky: #00aeef;
    --badge-blue: #29aae1;
    --ring-grey: #d1d3d4;
    --ink: #111;
    --muted: #555;
    --white: #fff;
  }
  html, body {
    margin: 0;
    width: 1200px;
    height: 1200px;
    overflow: hidden;
    background: var(--white);
  }
  .canvas { position: relative; width: 1200px; height: 1200px; }
  .intro {
    position: absolute; top: 160px; left: 0; width: 1200px;
    text-align: center; font-family: "Roboto Condensed", sans-serif;
  }
  .intro__title {
    margin: 0; font-size: 51px; font-weight: 700; color: var(--navy);
    letter-spacing: 0.5px; line-height: 1;
  }
  .intro__lede {
    margin: 10px 0 0; font-size: 19.5px; font-weight: 300; color: var(--muted);
    line-height: 26px; text-transform: uppercase;
  }
  .diagram { position: absolute; inset: 0; }
  .group-heading { font-family: "Roboto Condensed", sans-serif; font-size: 23px; fill: var(--ink); }
  .tile-title { font-family: "Roboto Condensed", sans-serif; font-weight: 700; font-size: 23px; fill: var(--white); }
  .tile-body { font-family: "Raleway", sans-serif; font-size: 18px; fill: var(--white); }
  .badge-name { font-family: "Roboto Condensed", sans-serif; font-weight: 700; font-size: 17px; fill: var(--white); }
  .hub-name { font-family: "Roboto Condensed", sans-serif; font-weight: 700; font-size: 34px; fill: var(--white); }
  .link { fill: none; stroke-width: 4; stroke-dasharray: 0 9; stroke-linecap: round; }
  .dots { fill: none; stroke-width: 4; stroke-dasharray: 0 9.4; stroke-linecap: round; }
</style>
</head>
<body>
<div class="canvas">
  <header class="intro">
    <h1 class="intro__title">MAPLE GROVE KINDERGARTEN</h1>
    <p class="intro__lede">Provides exceptional care and high-quality education for children aged six weeks to six years.<br>
      The modern centres have been designed to engage young children, with indoor learning spaces<br>
      and outdoor nature areas that will captivate your child’s imagination and<br>
      support their growth and development</p>
  </header>

  <svg class="diagram" viewBox="0 0 1200 1200" width="1200" height="1200">
    <text class="group-heading" x="332" y="450" text-anchor="middle">Brands &amp; Programs</text>
    <text class="group-heading" x="944" y="450" text-anchor="middle">Bloom Pathway 2.0 Curriculum</text>

    <!-- connectors -->
    <g class="links">
      <line class="link" x1="610" y1="772" x2="484" y2="523" stroke="var(--navy)"/>
      <line class="link" x1="610" y1="772" x2="380" y2="648" stroke="var(--ocean)"/>
      <line class="link" x1="610" y1="772" x2="300" y2="773" stroke="var(--teal)"/>
      <line class="link" x1="610" y1="772" x2="380" y2="898" stroke="var(--jade)"/>
      <line class="link" x1="610" y1="772" x2="484" y2="1022" stroke="var(--leaf)"/>
      <line class="link" x1="610" y1="772" x2="730" y2="523" stroke="var(--leaf)"/>
      <line class="link" x1="610" y1="772" x2="839" y2="648" stroke="var(--jade)"/>
      <line class="link" x1="610" y1="772" x2="918" y2="773" stroke="var(--teal)"/>
      <line class="link" x1="610" y1="772" x2="839" y2="898" stroke="var(--ocean)"/>
      <line class="link" x1="610" y1="772" x2="730" y2="1022" stroke="var(--navy)"/>
    </g>

    <!-- brand & program tiles -->
    <g class="tiles tiles--brands">
      <rect x="50" y="478" width="434" height="90" fill="var(--navy)"/>
      <text class="tile-title" x="374" y="506" text-anchor="end">Kestrel</text>
      <text class="tile-body" text-anchor="end"><tspan x="374" y="531">Nam pretium turpis et arcu. Duis</tspan><tspan x="374" y="553">arcu tortor, suscipit eget.</tspan></text>

      <rect x="50" y="602" width="330" height="90" fill="var(--ocean)"/>
      <text class="tile-title" x="280" y="630" text-anchor="end">Nest +</text>
      <text class="tile-body" text-anchor="end"><tspan x="280" y="653">Nam pretium turpis et</tspan><tspan x="280" y="675">arcu. Duis arcu tortor.</tspan></text>

      <rect x="50" y="727" width="250" height="90" fill="var(--teal)"/>
      <text class="tile-title" x="206" y="755" text-anchor="end">Tots +</text>
      <text class="tile-body"><tspan x="90" y="780">Nam pretium</tspan><tspan x="90" y="802">turpis et arcu.</tspan></text>

      <rect x="50" y="852" width="330" height="90" fill="var(--jade)"/>
      <text class="tile-title" x="274" y="880" text-anchor="end">DOVE</text>
      <text class="tile-body" text-anchor="end"><tspan x="277" y="907">Nam pretium turpis et</tspan><tspan x="277" y="929">arcu. Duis arcu tortor.</tspan></text>

      <rect x="50" y="977" width="434" height="90" fill="var(--leaf)"/>
      <text class="tile-title" x="380" y="1005" text-anchor="end">WREN</text>
      <text class="tile-body" text-anchor="end"><tspan x="376" y="1032">Nam pretium turpis et arcu. Duis</tspan><tspan x="376" y="1054">arcu tortor, suscipit eget.</tspan></text>
    </g>

    <!-- curriculum tiles -->
    <g class="tiles tiles--curriculum">
      <rect x="730" y="478" width="434" height="90" fill="var(--leaf)"/>
      <text class="tile-title" x="838" y="506">Keen Steps</text>
      <text class="tile-body"><tspan x="839" y="531">Nam pretium turpis et arcu. Duis</tspan><tspan x="839" y="552">arcu tortor, suscipit eget.</tspan></text>

      <rect x="839" y="602" width="325" height="90" fill="var(--jade)"/>
      <text class="tile-title" x="945" y="632">Curious</text>
      <text class="tile-body"><tspan x="949" y="656">Nam pretium turpis et</tspan><tspan x="949" y="677">arcu. Duis arcu tortor.</tspan></text>

      <rect x="918" y="727" width="246" height="90" fill="var(--teal)"/>
      <text class="tile-title" x="1026" y="758">Gather</text>
      <text class="tile-body"><tspan x="1028" y="782">Nam pretium</tspan><tspan x="1028" y="803">turpis et arcu.</tspan></text>

      <rect x="839" y="852" width="325" height="90" fill="var(--ocean)"/>
      <text class="tile-title" x="949" y="882">Move</text>
      <text class="tile-body"><tspan x="949" y="907">Nam pretium turpis et</tspan><tspan x="949" y="928">arcu. Duis arcu tortor.</tspan></text>

      <rect x="730" y="977" width="438" height="90" fill="var(--navy)"/>
      <text class="tile-title" x="834" y="1005">Tribe</text>
      <text class="tile-body"><tspan x="834" y="1032">Nam pretium turpis et arcu. Duis</tspan><tspan x="834" y="1053">arcu tortor, suscipit eget.</tspan></text>
    </g>

    <!-- brand badges -->
    <g class="badges badges--brands">
      <circle cx="484" cy="523" r="66" fill="var(--white)"/>
      <circle class="dots" cx="484" cy="523" r="58" stroke="var(--navy)"/>
      <circle cx="484" cy="523" r="50" fill="var(--badge-blue)"/>
      <text class="badge-name" x="484" y="529" text-anchor="middle">Kestrel</text>

      <circle cx="380" cy="648" r="66" fill="var(--white)"/>
      <circle class="dots" cx="380" cy="648" r="58" stroke="var(--ocean)"/>
      <circle cx="380" cy="648" r="50" fill="var(--badge-blue)"/>
      <circle cx="380" cy="648" r="36" fill="#f2c94c" opacity="0.85" role="img" aria-label="Illustration: open hand holding a red heart"/>

      <circle cx="300" cy="773" r="66" fill="var(--white)"/>
      <circle class="dots" cx="300" cy="773" r="58" stroke="var(--teal)"/>
      <circle cx="300" cy="773" r="50" fill="#6ccfdc"/>
      <circle cx="300" cy="773" r="36" fill="#f39a3a" opacity="0.8" role="img" aria-label="Illustration: two hands cupping an orange cross"/>

      <circle cx="380" cy="898" r="66" fill="var(--white)"/>
      <circle class="dots" cx="380" cy="898" r="58" stroke="var(--jade)"/>
      <circle cx="380" cy="898" r="50" fill="var(--badge-blue)"/>
      <text class="badge-name" x="380" y="904" text-anchor="middle">DOVE</text>

      <circle cx="484" cy="1022" r="66" fill="var(--white)"/>
      <circle class="dots" cx="484" cy="1022" r="58" stroke="var(--leaf)"/>
      <circle cx="484" cy="1022" r="50" fill="var(--badge-blue)"/>
      <text class="badge-name" x="484" y="1028" text-anchor="middle">WREN</text>
    </g>

    <!-- curriculum badges -->
    <g class="badges badges--curriculum">
      <circle cx="730" cy="523" r="66" fill="var(--white)"/>
      <circle class="dots" cx="730" cy="523" r="58" stroke="#9bd08a"/>
      <circle cx="730" cy="523" r="46" fill="var(--white)" stroke="var(--badge-blue)" stroke-width="7"/>
      <circle cx="730" cy="523" r="32" fill="#e8a25a" opacity="0.75" role="img" aria-label="Illustration: stack of colourful books"/>

      <circle cx="839" cy="648" r="66" fill="var(--white)"/>
      <circle class="dots" cx="839" cy="648" r="58" stroke="var(--jade)"/>
      <circle cx="839" cy="648" r="46" fill="var(--white)" stroke="var(--badge-blue)" stroke-width="7"/>
      <circle cx="839" cy="648" r="32" fill="#f5c04a" opacity="0.7" role="img" aria-label="Illustration: paintbrush with colourful paint dots"/>

      <circle cx="918" cy="773" r="66" fill="var(--white)"/>
      <circle class="dots" cx="918" cy="773" r="58" stroke="var(--teal)"/>
      <circle cx="918" cy="773" r="46" fill="var(--white)" stroke="var(--badge-blue)" stroke-width="7"/>
      <circle cx="918" cy="773" r="32" fill="#f7a530" opacity="0.8" role="img" aria-label="Illustration: two hands forming a heart"/>

      <circle cx="839" cy="898" r="66" fill="var(--white)"/>
      <circle class="dots" cx="839" cy="898" r="58" stroke="var(--ocean)"/>
      <circle cx="839" cy="898" r="46" fill="var(--white)" stroke="var(--badge-blue)" stroke-width="7"/>
      <circle cx="839" cy="898" r="32" fill="#e8403a" opacity="0.8" role="img" aria-label="Illustration: heart with pulse line, tennis ball and banana"/>

      <circle cx="730" cy="1022" r="66" fill="var(--white)"/>
      <circle class="dots" cx="730" cy="1022" r="58" stroke="var(--navy)"/>
      <circle cx="730" cy="1022" r="46" fill="var(--white)" stroke="var(--badge-blue)" stroke-width="7"/>
      <circle cx="730" cy="1022" r="32" fill="#d9b43a" opacity="0.7" role="img" aria-label="Illustration: three linked figures in a circle"/>
    </g>

    <!-- hub -->
    <g class="hub">
      <circle cx="610" cy="772" r="152" fill="var(--ring-grey)"/>
      <circle cx="610" cy="772" r="130" fill="var(--sky)"/>
      <text class="hub-name" text-anchor="middle"><tspan x="610" y="764">Maple Grove</tspan><tspan x="610" y="804">Kindergarten</tspan></text>
    </g>
  </svg>
</div>
</body>
</html>
```